Brochure for Specialist Divorce Support

1. I want an A4 three fold brochure or DL to promote my business and services.
My market are people going through divorce and are usually feeling very overwhelmed and therefore not functioning very well - both men and women, age early forties,
2. Colours – variety of blues and lime greens but you choose if you need a contrast e.g. orange
3. Images – happy single families
4. Theme - could you make it around water please - soothing
5. Logos – MJT &; MJR (I will attach)
6. I have a lot of content so maybe not too busy but still professional feel +
warm and reassuring
7. I'm attaching -

- a draft brochure I put together using a Microsoft template
- a word document with extra details
- plus two logos to do with my qualifications
- and some images for you to choose from

7. I want to use this as a template for some other brochures -> more work for
the winner.

Target Market(s)

Men and women usually in their early forties with primary school aged children i.e 5 to 12 years old.
They are going through a divorce and very upset, Maybe losing contact with their children and their way of life as they know it is disappearing. They are in turmoil and not functioning as well as they usually do.

Industry/Entity Type

Business

Font styles to use
Sans Serif

Colors
34a7d7
abd037
3277b5

Requirements
Must have
• I want the brochure to be three folds with the center the full A4
• Could you make the theme around water please.
• I will upload some photos for you to use if you want,

```html
<!DOCTYPE html>
<html lang="en">
<head>
<meta charset="utf-8">
<title>Specialist Divorce Support – Tri-fold Brochure</title>
<link href="https://fonts.googleapis.com/css2?family=Roboto+Condensed:ital,wght@0,300;0,400;0,700;1,400;1,700&family=Allura&display=swap" rel="stylesheet">
<style>
:root{
  --sky:#34a7d7;
  --lime:#abd037;
  --blue:#3277b5;
  --navy:#1d3d6e;
  --ink:#1e3552;
  --cream:#f4efe2;
  --stage:#1f5a8f;
}
*{box-sizing:border-box;margin:0;padding:0}
html,body{width:1200px;height:1200px;overflow:hidden}
body{background:var(--stage);font-family:'Roboto Condensed',sans-serif;color:var(--ink);position:relative}
.spread{position:absolute;left:220px;width:729px;height:567px;background:#fff;box-shadow:0 6px 18px rgba(0,0,0,.35);overflow:hidden}
.spread--outside{top:19px}
.spread--inside{top:610px}
.panel{position:absolute;top:0;height:567px;overflow:hidden}
.abs{position:absolute}
.photo{position:absolute}

/* outside: help panel */
.panel--help{left:0;width:242px;background:linear-gradient(160deg,#fff 35%,#dcedf8 70%,#c4e2f3 100%)}
.panel--help .photo{left:0;top:0;width:242px;height:200px;background:linear-gradient(180deg,#d9e98a 0%,#a7c948 55%,#7fae3a 100%)}
.panel--help h2{position:absolute;left:19px;top:191px;font-weight:400;font-size:20px;color:var(--navy)}
.help-list{position:absolute;left:21px;top:225px;width:216px;list-style:none}
.help-list li{font-size:10.2px;line-height:13px;color:var(--navy);height:39px;border-bottom:1px solid rgba(52,167,215,.35)}
.help-list li:last-child{border:none}

/* outside: coach panel */
.panel--coach{left:242px;width:240px;background:#f2f6e6}
.coach-lime{position:absolute;left:0;top:0;width:240px;height:320px;background:var(--lime)}
.testimonial{position:absolute;left:10px;top:34px;width:220px;text-align:center;font-size:7.8px;line-height:10.7px;color:#2a3516}
.testimonial p{margin-bottom:10px}
.testimonial b{font-style:italic}
.coach-name{position:absolute;left:12px;top:187px;font-size:18px;font-weight:300;color:#fff}
.coach-photo{left:11px;top:213px;width:53px;height:62px;border:2px solid #fff;background:linear-gradient(180deg,#cbd8b8,#9fae88)}
.creds{position:absolute;left:73px;top:213px;font-size:7.8px;line-height:10.8px;color:#1e2a12}
.coach-blue{position:absolute;left:0;top:300px;width:240px;height:158px}
.phone-text{position:absolute;left:30px;top:320px;width:205px;text-align:center;font-size:11.5px;line-height:15px;color:#fff}
.details{position:absolute;left:0;top:376px;width:240px;text-align:center;color:#fff;font-size:13.5px;line-height:18.2px;font-weight:300}
.details b{font-weight:700}
.coach-quote{position:absolute;left:14px;top:474px;width:220px;font-size:7.6px;line-height:10.5px;text-align:center;color:#222}
.coach-quote .mark{font-size:20px;font-weight:700;color:var(--navy);position:absolute;left:-10px;top:-6px}
.badges{position:absolute;left:28px;top:530px;width:200px;display:flex;justify-content:space-between;align-items:center}
.badge{display:flex;align-items:center;gap:4px;font-size:15px;font-weight:700;color:var(--navy)}
.badge i{width:10px;height:10px;background:var(--blue);display:block}
.badge i.round{border-radius:50%}

/* outside: cover */
.panel--cover{left:482px;width:247px;background:linear-gradient(180deg,#fff 0%,#fff 45%,#e9f4fb 100%)}
.brand{position:absolute;left:0;top:30px;width:247px;display:flex;justify-content:center;align-items:center;gap:8px;font-size:38px;font-weight:700;color:var(--navy);letter-spacing:1px}
.brand i{width:16px;height:16px;border-radius:50%;background:var(--blue);display:block}
.brand-sub{position:absolute;top:81px;width:247px;text-align:center;font-size:8px;color:var(--navy);letter-spacing:.5px}
.cover-title{position:absolute;top:98px;width:247px;text-align:center;font-weight:700;font-size:24px;line-height:28px;letter-spacing:1px}
.cover-title .a{color:var(--blue)}
.cover-title .b{color:var(--lime)}
.cover-sub{position:absolute;left:14px;top:155px;width:219px;text-align:center;font-size:12.4px;line-height:15px;color:#1a1a1a}
.script{position:absolute;left:38px;top:190px;font-family:'Allura',cursive;font-size:28px;line-height:26px;color:var(--navy);transform:rotate(-9deg)}
.cover-photo{left:0;top:255px;width:247px;height:200px;background:linear-gradient(180deg,#cfe6f3 0%,#9dcbe6 40%,#4aa3cf 62%,#e7ddc6 80%,#f3ecdc 100%)}
.cover-text{position:absolute;left:18px;top:460px;width:212px;text-align:center;font-style:italic;font-size:11.4px;line-height:15px;color:#2b2b2b}
.cover-url{position:absolute;top:527px;width:247px;text-align:center;font-weight:700;font-size:14px;color:var(--navy)}

/* inside */
.panel--services{left:0;width:482px;background:var(--cream)}
.services-photo{left:0;top:0;width:482px;height:340px;background:linear-gradient(180deg,#e8f2f6 0%,#bfdcc0 40%,#8cbf5c 75%,#f4efe2 100%)}
.lead-quote{position:absolute;left:24px;top:26px;width:132px;font-style:italic;font-size:8.8px;line-height:10.9px;text-align:center;color:#1a1a1a}
.lead-quote .mark{font-size:20px;font-weight:700;font-style:normal;color:var(--navy);position:absolute;left:-4px;top:-6px}
.services h2{position:absolute;left:266px;top:28px;font-size:37px;font-weight:400;color:var(--navy)}
.services-box{position:absolute;left:257px;top:78px;width:204px;height:248px;background:rgba(28,66,104,.88);padding:11px 6px 0 10px}
.services-box ul{list-style:none}
.services-box li{position:relative;padding-left:10px;font-size:9.5px;line-height:12px;color:#fff;margin-bottom:11px}
.services-box li::before,.bullets li::before{content:"";position:absolute;left:0;top:4px;width:4px;height:4px;border-radius:50%;background:currentColor}
.stages-title{position:absolute;left:27px;top:326px;font-size:24px;font-weight:400;color:var(--navy)}
.stage{position:absolute;left:27px;width:442px;font-size:9.3px;line-height:11.8px;color:#1a1a1a}
.stage h3{font-size:13px;font-weight:700;color:var(--navy);display:flex;align-items:center;gap:4px;margin-bottom:1px}
.stage h3 small{font-size:8.5px;color:var(--blue)}
.num{width:16px;height:16px;border-radius:50%;background:var(--lime);color:var(--navy);font-size:10px;display:inline-flex;align-items:center;justify-content:center;font-weight:700;flex:none}
.footer-band{position:absolute;left:0;top:520px;width:482px;height:47px;background:var(--lime);display:flex;align-items:center;padding-left:28px;font-size:14px;font-weight:700;letter-spacing:5.6px;color:var(--navy)}

.panel--skills{left:482px;width:247px;background:#fff}
.skills-head{position:absolute;left:12px;top:26px;width:230px;font-style:italic;font-weight:700;font-size:13.4px;line-height:15px;color:var(--navy)}
.bullets{list-style:none;position:absolute;left:10px;width:226px;font-size:9.4px;line-height:11.9px;color:#1a1a1a}
.bullets li{position:relative;padding-left:8px}
.bullets li::before{color:var(--navy);top:4px}
.skills-list{top:62px}
.stage3{position:absolute;left:10px;top:322px;width:226px}
.stage3 h3{font-size:13px;font-weight:700;color:var(--navy);line-height:13px}
.stage3 h3 small{font-size:8.7px;color:var(--blue)}
.stage3 .num{display:inline-flex;vertical-align:-2px}
.stage3-list{top:360px}
.skills-photo{left:0;top:418px;width:247px;height:149px;background:linear-gradient(120deg,#cfa987 0%,#e8d6c2 40%,#e9f1e0 70%,#cfe3ad 100%)}
.closing-quote{position:absolute;right:18px;top:428px;width:104px;text-align:right;font-size:16px;line-height:19.5px;color:#1a1a1a;font-weight:300}
.closing-quote b{font-style:italic;font-weight:700}
</style>
</head>
<body>

<section class="spread spread--outside">
  <div class="panel panel--help">
    <div class="photo" role="img" aria-label="Photo of a mother playing with two young children in a sunny meadow"></div>
    <svg class="abs" style="left:0;top:150px" width="242" height="70" viewBox="0 0 242 70">
      <path d="M0 70 L0 42 C60 10 150 -2 242 22 L242 70 Z" fill="#fff"/>
      <path d="M0 42 C60 10 150 -2 242 22 L242 30 C150 8 70 18 0 52 Z" fill="var(--lime)"/>
    </svg>
    <h2>Coaching can help you:</h2>
    <ul class="help-list">
      <li>Save money by being a more collected and credible client in the legal process</li>
      <li>Stay in control and focus on what's important for you and your family to avoid angry, emotional hijacks</li>
      <li>Feel more empowered by being organised and prepared for what's ahead and develop a plan of action</li>
      <li>Identify your next steps re: legal, financial, children's issues plus your self-care</li>
      <li>Develop a draft parenting plan to anticipate and address possible issues</li>
      <li>Consider areas of possible conflict and explore techniques to reduce confrontation</li>
      <li>Find your voice and be more confident in your skills to take control of your divorce and do it your way</li>
      <li>Let go of what was … and create what is possible during your divorce journey and afterwards.</li>
    </ul>
  </div>

  <div class="panel panel--coach">
    <div class="coach-lime"></div>
    <div class="testimonial">
      <p>"After many cups of coffee and long hours of listening to me, my very good friend suggested I speak to Marilyn, a divorce coach. I was a bit skeptical, especially when a phone session was suggested.</p>
      <p>From my first phone session I felt empowered. It gave me a sense of direction, assisted me to set realistic goals and action plans. Most importantly it aided my self esteem.</p>
      <p>Divorce is overwhelming. Talking to a caring professional like Maryanne helped me acknowledge my priorities and a way to achieve them. Thank you Maryanne."<br><b>- Rosalie</b></p>
    </div>
    <div class="coach-name">Maryanne</div>
    <div class="photo coach-photo" role="img" aria-label="Portrait photo of the coach seated outdoors"></div>
    <div class="creds">MJR Registered Separation Coach<br>Synergia Trained Conflict Coach<br>Cert IV in Training &amp; Assessment<br>Accredited in MJT Conflict Insight Profile<br>BA (Ind. Relations)</div>
    <svg class="coach-blue" viewBox="0 0 240 158" preserveAspectRatio="none">
      <path d="M0 38 C70 0 170 -4 240 28 L240 158 L0 158 Z" fill="var(--blue)"/>
      <path d="M60 14 C120 -2 190 4 240 26 L240 32 C180 10 120 6 60 14 Z" fill="#fff" opacity=".8"/>
      <path d="M0 38 C50 14 110 4 170 6 C110 12 50 26 0 46 Z" fill="var(--sky)"/>
      <path d="M20 40 c-6 2 -9 10 -6 20 c2 7 6 11 10 13 l4 -5 c-3 -2 -6 -6 -7 -10 c-1 -5 0 -9 3 -11 Z" fill="#fff"/>
    </svg>
    <div class="phone-text">Coaching works well over the phone, allowing for flexibility of time and place -evening appointments available.</div>
    <div class="details"><b>Full details are on:</b><br>SeparationCoachingHub.com.au<br><b>or email:</b><br>Marilyn@PartingWays.com.au</div>
    <div class="coach-quote"><span class="mark">“</span>Even the most together person can be totally unprepared for the emotional overwhelm that divorce can bring, regardless if they are the one who made the decision to leave."</div>
    <div class="badges">
      <span class="badge"><i></i>MJT</span>
      <span class="badge"><i class="round"></i>MJR</span>
    </div>
  </div>

  <div class="panel panel--cover">
    <div class="brand"><i></i>MJR</div>
    <div class="brand-sub">REGISTERED SEPARATION COACH</div>
    <div class="cover-title"><span class="a">SPECIALIST</span><br><span class="b">DIVORCE SUPPORT</span></div>
    <div class="cover-sub">Helping you move through this major life challenge so you can more successfully</div>
    <div class="script">Start living your<br>&nbsp;new life – your way!</div>
    <div class="photo cover-photo" role="img" aria-label="Photo of a mother walking hand in hand with two boys along the beach"></div>
    <div class="cover-text">Together we will identify your goals, set priorities and develop a plan for tomorrow … moving you through the pain of divorce to regain confidence and start anew.</div>
    <div class="cover-url">SeparationCoachingHub.com.au</div>
  </div>
</section>

<section class="spread spread--inside">
  <div class="panel panel--services services">
    <div class="photo services-photo" role="img" aria-label="Photo of a father and son playing soccer on a park lawn"></div>
    <div class="lead-quote"><span class="mark">“</span>Every divorce is different and families going forward will be different. I try to get my client to see or find ways they can co-parent as opposed to being one of two single parents."</div>
    <h2>Our Services</h2>
    <div class="services-box">
      <ul>
        <li>Specialist divorce support to suit your needs</li>
        <li>Pre-mediation coaching helping you prepare and achieve more positive outcomes to avoid going to court</li>
        <li>Collaborative law coaching to increase crucial skills so you can participate more constructively in negotiations</li>
        <li>Delivery of MJT Conflict Insight Profile giving you real feedback on the constructive and destructive behaviours you choose during conflict situations to facilitate more productive discussions</li>
        <li>Corporate Conflict Management Training</li>
      </ul>
    </div>
    <div class="stages-title">You will go through distinct stages:</div>
    <div class="stage" style="top:361px">
      <h3><span class="num">1</span>The Preparation Stage <small>– maybe entail one or two coaching sessions</small></h3>
      Anticipating all the unknowns and preparing before you see a Family Law Solicitor can save a lot of your solicitor's time and therefore money. The clearer you are on what you want to achieve throughout the process, the more specific legal advice you will receive.
    </div>
    <div class="stage" style="top:425px">
      <h3><span class="num">2</span>The Business Side of Divorce <small>– maybe two to four coaching sessions</small></h3>
      Divorce involves multiple areas of change, intensity of emotions, life changing decisions, loss of family structure and often a sense of isolation not experienced before.<br>
      The emotional overwhelm associated with relationship breakdown and the associated loss of 24/7 contact with children can impact even the most together person's ability to make well considered decisions.<br>
      Together, we will process emotions constructively and clarify decisions to be made... for you to be better able to communicate these in negotiations as well as set new boundaries.
    </div>
    <div class="footer-band">SeparationCoachingHub.com.au</div>
  </div>

  <div class="panel panel--skills">
    <div class="skills-head">Where necessary we can work on skills you will need for successful outcomes:</div>
    <ul class="bullets skills-list">
      <li>Conflict resolution skills plus specific verbal &amp; written communication skills important for more neutral emails and messages</li>
      <li>Having difficult conversations</li>
      <li>Preparing before attending joint conferences or mediation</li>
      <li>Managing anger</li>
      <li>Supporting your children to also navigate changed family structures</li>
      <li>Grieving losses ... even if you are the one who made the decision to leave</li>
      <li>Strategies for you to start healing and become whole again</li>
      <li>Drafting a parenting plan to anticipate &amp; address possible parenting issues, leading to more positive and successful co-parenting in the long term. <b>This is in everyone's interests... especially your children's.</b></li>
      <li>Look at possible stress strategies to sustain your energy levels, important for you to make good considered decisions</li>
    </ul>
    <div class="stage3"><h3><span class="num">3</span> The Moving On Stage <small>– one or two coaching sessions Dealing with endings and focusing on the future:</small></h3></div>
    <ul class="bullets stage3-list">
      <li>Changing your "self" image and building self worth</li>
      <li>Transitioning from married life to being single again</li>
      <li>Address barriers preventing you from moving forward</li>
      <li>Setting realistic goals to help transition to your new life more effectively</li>
    </ul>
    <div class="photo skills-photo" role="img" aria-label="Photo of a mother resting cheek to cheek with her young child"></div>
    <div class="closing-quote">“Everyone is <b>different</b> and moves through the stages at their <b>own pace."</b></div>
  </div>
</section>

</body>
</html>
```